Kestrel Dune Pictures Original Content TV Series & Reality TV, TV Commercials Movies Film Production

Hello Website revamp please. Would like a contemporary, simple, graphic, clean design, easy to navigate that highlights our skills in a remarkable design - might have to consider 2 sites, one that displays our long standing experience in film production service business, where we facilitate international film makers in SA. A second site that displays our work in development- where we create and conceptualise our own films and TV shows for the global market. Please see www.kdpictures.co.za for current website. Would like to retain the current red logo.

Target Market(s)

Film Studios

Coding

Number of Pages Required

2 page

Font styles to use
Sans Serif

Colors
ec1f27

Requirements
Must have
• Its own style
Nice to have
• Its own style
Should not have
• Template feeling to it

```html
<!DOCTYPE html>
<html lang="en">
<head>
<meta charset="utf-8">
<title>Kestrel Dune Pictures</title>
<link href="https://fonts.googleapis.com/css2?family=Public+Sans:wght@400;600;700;800&family=IBM+Plex+Sans:wght@300;400;500&display=swap" rel="stylesheet">
<style>
:root{
  --red:#ec1f27;
  --black:#000;
  --ink:#111;
  --white:#fff;
  --paper:#ececec;
  --mist:#f1f1f1;
  --muted:#444;
  --head:"Public Sans",sans-serif;
  --body:"IBM Plex Sans",sans-serif;
}
*{margin:0;padding:0;box-sizing:border-box}
html,body{width:1200px;height:3579px;overflow:hidden}
body{position:relative;font-family:var(--body);color:var(--ink);background:var(--white);-webkit-font-smoothing:antialiased;-moz-osx-font-smoothing:grayscale}
section,header,footer{position:absolute;left:0;width:1200px}
.abs{position:absolute}
.section-title{position:absolute;left:0;width:1200px;text-align:center;font-family:var(--head);font-weight:800;font-size:23px;letter-spacing:-.2px;color:var(--ink)}
.section-title::after{content:"";display:block;width:46px;height:3px;background:var(--red);margin:10px auto 0}
.btn{position:absolute;background:var(--red);color:var(--white);font-family:var(--head);font-weight:700;text-transform:uppercase;display:flex;align-items:center;justify-content:center}
.photo{position:absolute}

/* hero */
.hero{top:0;height:703px;background:#0b0b0b;overflow:hidden}
.hero-photo{left:0;top:0;width:1200px;height:703px;background:
  radial-gradient(ellipse 170px 60px at 500px 190px,#4a4a4a 0%,rgba(40,40,40,0) 100%),
  radial-gradient(ellipse 300px 330px at 540px 620px,#9a9a9a 0%,#5a5a5a 40%,rgba(20,20,20,0) 100%),
  radial-gradient(ellipse 520px 600px at 560px 420px,#2a2a2a 0%,#151515 60%,#0a0a0a 100%)}
.brand{left:38px;top:38px;display:flex;align-items:center;gap:10px}
.brand-ring{width:40px;height:40px;border-radius:50%;border:5px solid var(--red)}
.brand-name{font-family:var(--head);font-weight:700;font-size:17px;color:var(--white);text-transform:uppercase;width:120px;line-height:1.15}
.nav{right:36px;top:33px;display:flex;gap:28px;font-family:var(--body);font-size:14px;color:var(--white)}
.nav a{color:var(--white);text-decoration:none}
.nav a.active{color:var(--red);text-decoration:underline;text-underline-offset:4px;font-weight:500}
.hero-title{left:831px;top:208px;font-family:var(--head);font-weight:700;font-size:46px;color:var(--white);letter-spacing:.5px}
.hero-text{left:833px;top:279px;width:330px;font-size:14px;line-height:21px;color:var(--white);text-transform:uppercase}
.hero .btn{left:834px;top:342px;width:122px;height:39px;font-size:13.5px}
.dots{left:562px;top:661px;display:flex;gap:9px;align-items:center}
.dots span{width:7px;height:7px;border-radius:50%;background:var(--white)}
.dots span.on{width:10px;height:10px;background:var(--red);border:2px solid var(--white)}

/* services */
.services{top:703px;height:626px;background:var(--paper)}
.services .section-title{top:37px}
.service-card{position:absolute;top:108px;width:466px;height:471px;background:var(--white);box-shadow:0 2px 8px rgba(0,0,0,.08)}
.service-card .photo{left:0;top:0;width:466px;height:281px}
.service-card h3{position:absolute;left:37px;top:311px;font-family:var(--head);font-weight:700;font-size:16px;text-transform:uppercase}
.service-card p{position:absolute;left:37px;top:345px;width:380px;font-size:13px;line-height:19px;color:var(--muted)}
.service-card .btn{left:37px;top:404px;width:94px;height:31px;font-size:11px}

/* about */
.about{top:1329px;height:467px;background:var(--black)}
.about-ring{left:165px;top:55px;width:362px;height:362px;border-radius:50%;border:12px solid var(--red);overflow:hidden}
.about-ring .photo{inset:0;background:
  radial-gradient(ellipse 90px 70px at 170px 130px,#3b46e0 0%,rgba(40,50,200,0) 100%),
  radial-gradient(ellipse 110px 80px at 190px 250px,#d8d8dc 0%,rgba(200,200,205,0) 100%),
  linear-gradient(180deg,#1e2238 0%,#2c2f58 45%,#55586a 75%,#1a1a1a 100%)}
.about h2{position:absolute;left:601px;top:55px;font-family:var(--head);font-weight:800;font-size:23px;color:var(--white)}
.about h2::after{content:"";display:block;width:46px;height:3px;background:var(--red);margin-top:9px}
.about-text{position:absolute;left:601px;top:131px;width:452px;font-family:var(--body);font-weight:400;font-size:16px;line-height:24px;color:#f2f2f2}
.about .btn{left:604px;top:362px;width:105px;height:33px;font-size:12px}

/* films */
.films{top:1796px;height:725px;background:var(--white)}
.films .section-title{top:41px}
.film{position:absolute;width:304px}
.film .photo{position:relative;width:304px;height:239px}
.film h4{margin-top:16px;text-align:center;font-family:var(--head);font-weight:700;font-size:13px;text-transform:uppercase}

/* television */
.tv{top:2521px;height:327px;background:var(--mist)}
.tv .section-title{top:36px}
.tv-card{position:absolute;top:103px;width:304px;height:178px;background:var(--white);display:flex;align-items:center;justify-content:center;gap:10px}
.tv-card span{font-family:var(--head);font-weight:700;font-size:24px;color:#2b2b2b;text-transform:uppercase;text-align:center;line-height:1.1}
.tv-card i{width:18px;height:18px;border-radius:50%;background:var(--red);flex:none}
.arrow{position:absolute}

/* commercials */
.commercials{top:2848px;height:383px;background:var(--white)}
.commercials .section-title{top:44px}
.ad{position:absolute;top:108px;width:304px;height:226px}

/* footer */
.footer{top:3231px;height:348px;background:var(--black);color:var(--white)}
.footer-brand{left:133px;top:52px;display:flex;align-items:center;gap:12px}
.footer-brand .brand-ring{width:48px;height:48px;border-width:6px}
.footer-brand .brand-name{font-size:19px;width:150px}
.footer h5{position:absolute;top:50px;font-family:var(--head);font-weight:700;font-size:12px;letter-spacing:.3px}
.menu-list{position:absolute;left:413px;top:87px;list-style:none;font-size:12px;line-height:20px;text-transform:uppercase}
.contact-row,.social-row{position:absolute;display:flex;align-items:center;gap:10px;font-size:12px;line-height:16px}
.icon{width:22px;height:22px;border-radius:50%;background:var(--white);display:flex;align-items:center;justify-content:center;flex:none}
.footer-rule{left:133px;top:265px;width:934px;height:1px;background:#2a2a2a}
.copyright{left:0;top:298px;width:1200px;text-align:center;font-size:10px;color:#ddd}
</style>
</head>
<body>

<header class="hero">
  <div class="photo hero-photo" role="img" aria-label="Moody black and white portrait of a man in a fedora and trench coat"></div>
  <div class="abs brand"><div class="brand-ring"></div><div class="brand-name">Kestrel Dune Pictures</div></div>
  <nav class="abs nav">
    <a class="active" href="#">HOME</a><a href="#">COMMERCIALS</a><a href="#">FILMS</a><a href="#">TELEVISION</a><a href="#">CONTACT</a>
  </nav>
  <h1 class="abs hero-title">FILMS</h1>
  <p class="abs hero-text">Lorem ipsum is simply dummy text of the printing and typesetting industry</p>
  <a class="btn">Read More</a>
  <div class="abs dots"><span></span><span></span><span class="on"></span><span></span><span></span></div>
</header>

<section class="services">
  <h2 class="section-title">OUR SERVICES</h2>
  <article class="service-card" style="left:131px">
    <div class="photo" role="img" aria-label="Film clapperboard in red and blue smoke" style="background:radial-gradient(ellipse 180px 110px at 180px 60px,#5a6ad0 0%,rgba(60,70,180,0) 100%),radial-gradient(ellipse 200px 140px at 400px 120px,#e0202a 0%,rgba(200,20,30,0) 100%),linear-gradient(135deg,#0a1230 0%,#14204a 45%,#3a1030 75%,#6a0a12 100%)"></div>
    <h3>Film Production</h3>
    <p>Lorem Ipsum is simply dummy text of the printing and typesetting industry. Lorem Ipsum has bee.</p>
    <a class="btn">Read More</a>
  </article>
  <article class="service-card" style="left:619px">
    <div class="photo" role="img" aria-label="Hand holding a remote in front of a wall of TV screens" style="background:radial-gradient(ellipse 160px 120px at 160px 140px,#d9b24a 0%,rgba(200,160,70,0) 100%),radial-gradient(ellipse 140px 110px at 330px 110px,#4d8fbf 0%,rgba(70,130,180,0) 100%),linear-gradient(135deg,#26303a 0%,#4a5866 50%,#2a2e34 100%)"></div>
    <h3>Conceptualise Our Own Films and TV Shows</h3>
    <p>Lorem Ipsum is simply dummy text of the printing and typesetting industry. Lorem Ipsum has bee.</p>
    <a class="btn">Read More</a>
  </article>
</section>

<section class="about">
  <div class="abs about-ring"><div class="photo" role="img" aria-label="Camera crew filming a studio talk show"></div></div>
  <h2>ABOUT US</h2>
  <p class="about-text">Sed ut perspiciatis unde omnis iste natus error sit voluptatem accusantium doloremque laudantium, totam rem aperiam, eaque ipsa quae ab illo inventore veritatis et quasi architecto beatae vitae dicta sunt explicabo. Nemo enim ipsam voluptatem quia voluptas sit aspernatur aut odit aut fugit, sed quia consequuntur magni dolores eos qui ratione voluptatem sequi nesciunt. Neque porro quisquam est, qui dolorem ipsum quia dolor sit amet</p>
  <a class="btn">Read More</a>
</section>

<section class="films">
  <h2 class="section-title">FILMS</h2>
  <figure class="film" style="left:131px;top:110px"><div class="photo" role="img" aria-label="Comedy film poster with a group of characters" style="background:radial-gradient(ellipse 120px 70px at 180px 190px,#d89a2a 0%,rgba(200,140,40,0) 100%),linear-gradient(180deg,#9aa8b4 0%,#8a6a58 40%,#8a3a2a 75%,#3a2418 100%)"></div><h4>Red Harbour</h4></figure>
  <figure class="film" style="left:449px;top:110px"><div class="photo" role="img" aria-label="Desert mountain landscape poster" style="background:radial-gradient(ellipse 200px 70px at 180px 150px,#b8a88c 0%,rgba(170,150,120,0) 100%),linear-gradient(180deg,#9a8e78 0%,#6c5e4a 45%,#4e4232 100%)"></div><h4>Dust Road</h4></figure>
  <figure class="film" style="left:765px;top:110px"><div class="photo" role="img" aria-label="Adventure comedy poster on the savanna" style="background:radial-gradient(ellipse 90px 110px at 150px 130px,#c8a070 0%,rgba(200,160,110,0) 100%),linear-gradient(180deg,#1f5ab4 0%,#4a86cc 55%,#d0a048 85%,#8a6a30 100%)"></div><h4>Savanna Run</h4></figure>
  <figure class="film" style="left:131px;top:405px"><div class="photo" role="img" aria-label="Night driving scene still" style="background:radial-gradient(ellipse 70px 90px at 80px 120px,#6a5a48 0%,rgba(80,70,50,0) 100%),radial-gradient(ellipse 110px 40px at 220px 200px,#7a5a20 0%,rgba(100,70,20,0) 100%),linear-gradient(135deg,#1e2418 0%,#0e120e 60%,#1a1408 100%)"></div><h4>Night Drive</h4></figure>
  <figure class="film" style="left:449px;top:405px"><div class="photo" role="img" aria-label="Black and white crime film poster" style="background:radial-gradient(ellipse 90px 110px at 160px 110px,#8a8a8a 0%,rgba(120,120,120,0) 100%),linear-gradient(180deg,#6a6a6a 0%,#3a3a3a 50%,#121212 100%)"></div><h4>The Last Crew</h4></figure>
  <figure class="film" style="left:765px;top:405px"><div class="photo" role="img" aria-label="Man in a suit holding a weapon, game still" style="background:radial-gradient(ellipse 70px 110px at 140px 150px,#3a3e42 0%,rgba(50,55,60,0) 100%),radial-gradient(ellipse 60px 40px at 260px 60px,#8a4a3a 0%,rgba(120,60,50,0) 100%),linear-gradient(160deg,#3a4248 0%,#1e2428 60%,#0e1012 100%)"></div><h4>Silent Contract</h4></figure>
</section>

<section class="tv">
  <h2 class="section-title">TELEVISION</h2>
  <svg class="arrow" style="left:76px;top:180px" width="16" height="28" viewBox="0 0 16 28"><path d="M13 2 3 14l10 12" fill="none" stroke="#9a9a9a" stroke-width="2.5"/></svg>
  <svg class="arrow" style="left:1106px;top:180px" width="16" height="28" viewBox="0 0 16 28"><path d="M3 2l10 12L3 26" fill="none" stroke="#9a9a9a" stroke-width="2.5"/></svg>
  <div class="tv-card" style="left:131px"><span>Coastline<br>Lives</span></div>
  <div class="tv-card" style="left:444px"><i></i><span>Kitchen Duel</span></div>
  <div class="tv-card" style="left:765px"><span>Stadium<br>Stories</span></div>
</section>

<section class="commercials">
  <h2 class="section-title">COMMERCIALS</h2>
  <svg class="arrow" style="left:76px;top:217px" width="16" height="28" viewBox="0 0 16 28"><path d="M13 2 3 14l10 12" fill="none" stroke="#9a9a9a" stroke-width="2.5"/></svg>
  <svg class="arrow" style="left:1106px;top:217px" width="16" height="28" viewBox="0 0 16 28"><path d="M3 2l10 12L3 26" fill="none" stroke="#9a9a9a" stroke-width="2.5"/></svg>
  <div class="ad" style="left:131px;background:radial-gradient(ellipse 160px 60px at 150px 170px,#7a2a4a 0%,rgba(110,40,70,0) 100%),radial-gradient(ellipse 70px 50px at 160px 170px,#1f7a7a 0%,rgba(30,120,120,0) 100%),linear-gradient(180deg,#cfdce6 0%,#b4c4d0 45%,#6a4a5a 80%,#3a2a3a 100%)" role="img" aria-label="Row of shampoo bottles advert"></div>
  <div class="ad" style="left:447px;background:radial-gradient(ellipse 60px 110px at 60px 110px,#e8a050 0%,rgba(220,150,80,0) 100%),radial-gradient(ellipse 110px 40px at 200px 180px,#c88a3a 0%,rgba(200,130,60,0) 100%),linear-gradient(135deg,#2a1c12 0%,#5a3a20 50%,#3a2616 100%)" role="img" aria-label="Insect bite gel advert with tubes"></div>
  <div class="ad" style="left:765px;background:radial-gradient(ellipse 90px 60px at 110px 120px,#2a4ab8 0%,rgba(40,70,180,0) 100%),radial-gradient(ellipse 40px 30px at 280px 180px,#d0302a 0%,rgba(200,40,40,0) 100%),linear-gradient(180deg,#2f9ad6 0%,#6cbde6 45%,#e6eef2 75%,#cfdde4 100%)" role="img" aria-label="Yoghurt competition advert with island scene"></div>
</section>

<footer class="footer">
  <div class="abs footer-brand"><div class="brand-ring"></div><div class="brand-name">Kestrel Dune Pictures</div></div>

  <h5 style="left:413px">MENU</h5>
  <ul class="menu-list"><li>Home</li><li>Commercials</li><li>Films</li><li>Television</li><li>Contact</li></ul>

  <h5 style="left:671px">CONTACT US</h5>
  <div class="contact-row" style="left:669px;top:86px">
    <span class="icon"><svg width="12" height="12" viewBox="0 0 24 24"><path d="M6.6 10.8a15 15 0 0 0 6.6 6.6l2.2-2.2a1 1 0 0 1 1-.25 11.4 11.4 0 0 0 3.6.57 1 1 0 0 1 1 1V20a1 1 0 0 1-1 1A17 17 0 0 1 3 4a1 1 0 0 1 1-1h3.5a1 1 0 0 1 1 1c0 1.25.2 2.45.57 3.57a1 1 0 0 1-.25 1z" fill="#000"/></svg></span>
    <span>Call Us<br>+27(0) 21 555 0142</span>
  </div>
  <div class="contact-row" style="left:669px;top:135px">
    <span class="icon"><svg width="12" height="12" viewBox="0 0 24 24"><path d="M3 5h18v14H3z" fill="#000"/><path d="M3 5l9 7 9-7" fill="none" stroke="#fff" stroke-width="2"/></svg></span>
    <span>E mail Us<br>info@kdpictures.co.za</span>
  </div>

  <h5 style="left:961px">FOLLOW US</h5>
  <div class="social-row" style="left:961px;top:86px"><span class="icon"></span><span>Like us on<br>CINEFEED</span></div>
  <div class="social-row" style="left:961px;top:135px"><span class="icon"></span><span>Follow us on<br>CLIPWIRE</span></div>
  <div class="social-row" style="left:961px;top:186px"><span class="icon"></span><span>Follow us on<br>CREWLINK</span></div>

  <div class="abs footer-rule"></div>
  <p class="abs copyright">Copyright © 2021 All Rights Reserved</p>
</footer>

</body>
</html>
```